Food supplement packaging for functional chewing

We need a design of 2 boxes of a food supplement in functional chewing gum for Immune system enhancement and a multivitamin complex. Both products can be used by adults and children above 7. Products will be sold online.
More information in attached. PDF of similar product with dimensions of the box and the company logo also in attached. We would like that the design follows somehow the graphics of the existing product.

Target Market(s)

Families that seek health

Industry/Entity Type

Pharmaceuticals

Requirements
Nice to have
• vivid colours

```html
<!DOCTYPE html>
<html lang="it">
<head>
<meta charset="utf-8">
<title>Omnivit Gum – confezione</title>
<link href="https://fonts.googleapis.com/css2?family=Archivo+Black&family=Roboto:wght@700;900&display=swap" rel="stylesheet">
<style>
  :root {
    --backdrop: #e8e8e8;
    --purple-deep: #6a1f9a;
    --purple: #8a2aa8;
    --magenta: #c42d9e;
    --label-green: #6cc24a;
    --badge-green: #4fae3a;
    --name-white: #f4f4f4;
    --sub-yellow: #f2e35a;
    --placeholder-grey: #8f8f8f;
  }
  * { margin: 0; padding: 0; box-sizing: border-box; }
  html, body { width: 1200px; height: 917px; overflow: hidden; background: var(--backdrop); }
  .canvas { position: relative; width: 1200px; height: 917px; }

  .box-front {
    position: absolute; left: 100px; top: 208px; width: 1000px; height: 500px;
    background: linear-gradient(115deg, var(--purple-deep) 0%, var(--purple) 40%, var(--magenta) 100%);
    overflow: hidden;
  }

  .claim-label {
    position: absolute; left: 24px; top: 140px; width: 340px; padding: 10px 14px;
    background: var(--label-green); color: #fff;
    font-family: "Roboto", sans-serif; font-weight: 700; font-size: 15px; line-height: 1.25;
  }
  .claim-label .claim-strong { font-weight: 900; font-size: 16px; margin-top: 4px; }

  .brand {
    position: absolute; left: 28px; top: 236px; display: flex; align-items: center; gap: 12px;
    font-family: "Archivo Black", sans-serif; font-size: 34px; color: #ffffff;
  }
  .brand-dot { width: 34px; height: 34px; border-radius: 50%; background: #ffffff; }

  .product-name {
    position: absolute; left: 28px; top: 292px;
    font-family: "Archivo Black", sans-serif; font-size: 72px; line-height: 0.95;
    color: var(--name-white); letter-spacing: 1px;
  }
  .pack-size {
    position: absolute; left: 30px; top: 440px;
    font-family: "Archivo Black", sans-serif; font-size: 26px; color: var(--sub-yellow);
  }

  .seal-spot {
    position: absolute; left: 410px; top: 50px; width: 150px; height: 150px;
    border-radius: 50%; background: var(--placeholder-grey);
  }

  .runners-art {
    position: absolute; left: 580px; top: 225px; width: 300px; height: 150px;
    border-radius: 40px;
    background: linear-gradient(90deg, rgba(120,200,70,.55), rgba(240,220,60,.55), rgba(255,255,255,.55));
  }

  .free-badges { position: absolute; right: 40px; top: 28px; display: flex; flex-direction: column; gap: 26px; }
  .free-badge {
    width: 62px; height: 62px; border-radius: 50%; background: var(--badge-green);
    display: flex; flex-direction: column; align-items: center; justify-content: center;
    font-family: "Roboto", sans-serif; font-weight: 900; color: #fff; line-height: 1.05; text-align: center;
  }
  .free-badge .badge-main { font-size: 10px; letter-spacing: .3px; }
  .free-badge .badge-sub { font-size: 9px; font-weight: 700; }
</style>
</head>
<body>
<div class="canvas">
  <section class="box-front">
    <div class="claim-label">
      <p>Integratore alimentare Multivitaminico<br>in chewing gum</p>
      <p class="claim-strong">12 VITAMINE PER TUTTA LA FAMIGLIA</p>
    </div>

    <div class="brand"><span class="brand-dot"></span><span>Kavela Labs</span></div>

    <h1 class="product-name">OMNIVIT<br>GUM</h1>
    <p class="pack-size">10 chewing gum da 2g</p>

    <div class="seal-spot"></div>

    <div class="runners-art" role="img" aria-label="Illustrazione di tre sagome di corridori in verde, giallo e bianco"></div>

    <div class="free-badges">
      <div class="free-badge"><span class="badge-main">SUGAR</span><span class="badge-sub">free</span></div>
      <div class="free-badge"><span class="badge-main">LACTOSE</span><span class="badge-sub">free</span></div>
      <div class="free-badge"><span class="badge-main">GLUTEN</span><span class="badge-sub">free</span></div>
    </div>
  </section>
</div>
</body>
</html>
```